依頼詳細
写真挿入は無し、メニュー、営業時間も別看板がありますので記載不要です。添付のロゴとイラストを挿入してください。看板は両面ですが1デザインでも構いません。
記載項目
記載項目
⚪店名 月灯りこまち
⚪定食 お酒 または、お食事 呑み処 など(デザインとのバランスでお願いします。)
⚪お気軽にどうぞ、気軽に来店ください など(安心して気軽に入店しやすくなる1フレーズ)
⚪イラストにふき出しで発声させてください。(フレーズはお任せします。)
⚪サイズは450mm×1300mmで縦長です。納品はaiデータです。
⚪文字色、全体的なデザインはお任せですが、背景色は薄ピンクが希望色です。グラデーションも好きです。イラスト、ロゴとのバランスでお願いします。
希望イメージ
シンプル 複雑
単色 カラフル
暗い 明るい
日常 高級
遊び心 厳粛
未来的 伝統的
女性的 男性的
希望する色
納品ファイル
• イラストレーター形式 (.ai)
補足説明
私ai使えませんので確認は別形式でお願いします。
選定確約有りに変更しました。

見やすくバランスが良く丁度良いです。

また、よろしくお願いいたします。

```html
<!DOCTYPE html>
<html lang="ja">
<head>
<meta charset="utf-8">
<title>月灯りこまち のぼり</title>
<link rel="stylesheet" href="https://fonts.googleapis.com/css2?family=Shippori+Mincho+B1:wght@700;800&family=M+PLUS+Rounded+1c:wght@800&display=swap">
<style>
  :root {
    --bg-light: #fff6f8;
    --bg-pink: #f9d6df;
    --bg-deep: #f2b3c3;
    --plum: #8a1f52;
    --name: #7c2248;
    --blush: #f1a7bb;
    --bubble: #e8799a;
    --blossom: #f6c3d0;
    --blossom-deep: #ee9fb4;
    --kimono: #a9c48e;
    --hair: #f2a9c0;
    --white: #ffffff;
  }
  html, body {
    margin: 0;
    padding: 0;
    width: 1200px;
    height: 3464px;
    overflow: hidden;
  }
  .banner {
    position: relative;
    width: 1200px;
    height: 3464px;
    overflow: hidden;
    background: linear-gradient(180deg, var(--bg-pink) 0%, var(--bg-light) 18%, var(--bg-light) 55%, var(--bg-pink) 80%, var(--bg-deep) 100%);
  }
  .blossom-cluster {
    position: absolute;
    border-radius: 50%;
    background: radial-gradient(closest-side, var(--blossom-deep), var(--blossom) 55%, rgba(246,195,208,0) 100%);
    opacity: .8;
  }
  .blossom-top-left { left: -200px; top: -160px; width: 640px; height: 520px; }
  .blossom-top-right { left: 760px; top: -120px; width: 640px; height: 900px; }
  .blossom-right { left: 900px; top: 720px; width: 480px; height: 900px; }
  .blossom-mid-left { left: -220px; top: 1700px; width: 480px; height: 700px; opacity: .5; }
  .blossom-bottom-left { left: -180px; top: 2900px; width: 760px; height: 700px; }

  .category {
    position: absolute;
    left: 380px;
    top: 180px;
    width: 480px;
    height: 440px;
    border-top: 10px solid var(--plum);
    border-bottom: 10px solid var(--plum);
    display: flex;
    flex-direction: row-reverse;
    justify-content: center;
    align-items: center;
    gap: 40px;
  }
  .category-line {
    writing-mode: vertical-rl;
    font-family: "Shippori Mincho B1", serif;
    font-weight: 800;
    font-size: 128px;
    line-height: 1;
    letter-spacing: 4px;
    color: var(--plum);
    margin: 0;
  }

  .name-glow {
    position: absolute;
    left: 180px;
    top: 1200px;
    width: 760px;
    height: 720px;
    border-radius: 50%;
    background: radial-gradient(closest-side, var(--blush), rgba(241,167,187,.45) 55%, rgba(241,167,187,0) 100%);
  }
  .shop-name {
    position: absolute;
    inset: 0;
    margin: 0;
    font-family: "Shippori Mincho B1", serif;
    font-weight: 800;
    color: var(--name);
    pointer-events: none;
  }
  .name-char {
    position: absolute;
    display: block;
    line-height: 1;
  }
  .char-1 { left: 220px; top: 980px;  font-size: 250px; }
  .char-2 { left: 470px; top: 960px;  font-size: 250px; }
  .char-3 { left: 730px; top: 990px;  font-size: 250px; }
  .char-4 { left: 250px; top: 1300px; font-size: 230px; }
  .char-5 { left: 440px; top: 1500px; font-size: 280px; }
  .char-6 { left: 440px; top: 1820px; font-size: 280px; }

  .shop-roman {
    position: absolute;
    left: 720px;
    top: 1900px;
    font-family: "Shippori Mincho B1", serif;
    font-weight: 800;
    font-size: 58px;
    line-height: 1.15;
    color: var(--name);
    letter-spacing: 2px;
    margin: 0;
  }
  .shop-seal {
    position: absolute;
    left: 260px;
    top: 2230px;
    width: 52px;
    height: 66px;
    background: var(--name);
  }

  .speech-bubble {
    position: absolute;
    left: 80px;
    top: 2520px;
    width: 420px;
    height: 460px;
  }
  .speech-text {
    position: absolute;
    left: 80px;
    top: 2650px;
    width: 420px;
    margin: 0;
    text-align: center;
    font-family: "M PLUS Rounded 1c", sans-serif;
    font-weight: 800;
    font-size: 64px;
    line-height: 1.3;
    color: var(--white);
  }

  .character-art {
    position: absolute;
    left: 600px;
    top: 2340px;
    width: 580px;
    height: 1124px;
    border-radius: 260px 260px 0 0;
    background: linear-gradient(180deg, var(--hair) 0%, #f7c9d6 30%, var(--kimono) 55%, #b7cfa0 75%, var(--blossom-deep) 100%);
    opacity: .9;
  }
</style>
</head>
<body>
  <main class="banner">
    <div class="blossom-cluster blossom-top-left" role="img" aria-label="桜の花の装飾"></div>
    <div class="blossom-cluster blossom-top-right" role="img" aria-label="桜の花の装飾"></div>
    <div class="blossom-cluster blossom-right" role="img" aria-label="桜の花の装飾"></div>
    <div class="blossom-cluster blossom-mid-left" role="img" aria-label="桜の花の装飾"></div>
    <div class="blossom-cluster blossom-bottom-left" role="img" aria-label="桜の花の装飾"></div>

    <header class="category">
      <p class="category-line">お食事</p>
      <p class="category-line">呑み処</p>
    </header>

    <div class="name-glow"></div>
    <h1 class="shop-name" aria-label="月灯りこまち">
      <span class="name-char char-1" aria-hidden="true">月</span>
      <span class="name-char char-2" aria-hidden="true">灯</span>
      <span class="name-char char-3" aria-hidden="true">り</span>
      <span class="name-char char-4" aria-hidden="true">こ</span>
      <span class="name-char char-5" aria-hidden="true">ま</span>
      <span class="name-char char-6" aria-hidden="true">ち</span>
    </h1>
    <p class="shop-roman">tsukiakari<br>komachi</p>
    <div class="shop-seal"></div>

    <div class="character-art" role="img" aria-label="着物姿の桜髪の女の子のイラスト"></div>

    <svg class="speech-bubble" viewBox="0 0 420 460" aria-hidden="true">
      <path fill="var(--bubble)" d="M210 40 C250 0 330 20 330 90 C400 80 440 160 390 210 C440 260 400 350 330 330 C330 400 260 430 220 390 L200 460 L180 385 C140 430 70 400 80 330 C10 350 -20 260 30 210 C-20 160 20 80 90 90 C90 20 170 0 210 40 Z"/>
    </svg>
    <p class="speech-text">お気軽に<br>どうぞ!!</p>
  </main>
</body>
</html>
```